Flyer Ballettschule
Vielen Dank für den wirklich sehr professionellen superschönen Flyer. Uns hat das Design beim ersten Entwurf schon perfekt gefallen. Sofort hat der Designer kleine Änderungen bestens umgesetzt. Sehr netter Kontakt. Ein ganz großes Dankeschön! Ballettschule Wendelmoor

```html
<!DOCTYPE html>
<html lang="de">
<head>
<meta charset="utf-8">
<title>Flyer Ballettschule Wendelmoor</title>
<link href="https://fonts.googleapis.com/css2?family=Arimo:ital,wght@0,400;0,700;1,400&family=Cormorant+Garamond:ital,wght@1,600;1,700&display=swap" rel="stylesheet">
<style>
:root{
  --red:#e2141c;
  --grey:#7c7d7f;
  --ink:#111;
  --muted:#7a7a7a;
  --white:#fff;
  --floor:#e6e6e4;
  --script:"Cormorant Garamond", serif;
  --sans:"Arimo", Arial, sans-serif;
}
html,body{margin:0;padding:0;width:1188px;height:1200px;overflow:hidden;background:var(--white);}
.flyer{position:relative;width:1188px;height:1200px;overflow:hidden;font-family:var(--sans);color:var(--ink);}
.panel{position:absolute;top:0;height:1200px;overflow:hidden;background:var(--white);}
.panel--front{left:0;width:555px;}
.panel--back{left:629px;width:559px;}
.abs{position:absolute;}
.photo{position:absolute;left:0;width:100%;background:linear-gradient(180deg,#d9d9d7 0%,#ecebea 45%,#e3e3e1 100%);}
.photo--strip{top:0;height:23px;}
.photo--hero{top:165px;height:209px;}
.brand{position:absolute;display:flex;align-items:center;gap:12px;}
.brand__dot{width:22px;height:22px;border-radius:50%;background:var(--red);flex:none;}
.brand__name{font-family:var(--script);font-style:italic;font-weight:600;color:var(--ink);line-height:1;}
.brand--top{left:150px;top:72px;}
.brand--top .brand__name{font-size:34px;}
.brand--bottom{left:175px;top:1096px;}
.brand--bottom .brand__name{font-size:24px;}

.band-red{position:absolute;top:374px;left:0;width:100%;height:112px;background:var(--red);color:var(--white);}
.anniv{position:absolute;left:44px;top:18px;font-family:var(--script);font-style:italic;font-weight:600;white-space:nowrap;}
.anniv__big{font-size:44px;}
.anniv__small{font-size:21px;margin-left:6px;}
.invite{position:absolute;left:41px;top:66px;font-weight:700;font-size:22px;}

.offer{position:absolute;left:41px;width:500px;}
.offer h3{margin:0;font-size:17.5px;font-weight:700;line-height:24px;}
.offer ul{list-style:none;margin:0;padding:0;}
.offer li{position:relative;padding-left:14px;font-size:17.5px;line-height:24.2px;}
.offer li::before{content:"";position:absolute;left:2px;top:10px;width:5px;height:5px;border-radius:50%;background:var(--red);}
.offer--kids{top:500px;}
.offer--adults{top:741px;}
.note{font-style:italic;font-size:14.5px;}

.footer{position:absolute;left:0;top:896px;width:100%;height:304px;}
.footer svg{position:absolute;left:0;top:0;}
.contact{position:absolute;left:44px;top:18px;color:var(--white);}
.contact__name{font-family:var(--script);font-style:italic;font-weight:600;font-size:25px;line-height:30px;}
.contact__lines{font-size:15.5px;line-height:20.2px;margin-top:0;}
.contact__web{font-size:15.5px;line-height:20.5px;margin-top:16px;}
.contact__member{font-family:var(--script);font-style:italic;font-weight:600;font-size:25px;margin-top:10px;}

.quote{position:absolute;left:44px;top:36px;font-family:var(--script);font-style:italic;font-weight:700;color:var(--red);font-size:46px;line-height:54px;}
.quote__second{padding-left:26px;}
.band-grey{position:absolute;top:374px;left:0;width:100%;height:112px;background:var(--grey);color:var(--white);}
.band-grey p{margin:0;position:absolute;left:46px;top:11px;font-family:var(--script);font-style:italic;font-weight:600;font-size:24.5px;line-height:28.5px;}
.gallery{position:absolute;top:489px;height:187px;}
.gallery--costumes{left:0;width:276px;background:linear-gradient(135deg,#c9d3b4 0%,#b2243f 40%,#2b2e4d 65%,#7a5a3b 100%);}
.gallery--stage{left:280px;width:279px;background:linear-gradient(160deg,#a2543e 0%,#e6d9df 40%,#e06aa2 70%,#6d5650 100%);}
.benefits{position:absolute;left:46px;top:688px;width:500px;}
.benefits h3{margin:0 0 12px;font-size:17.5px;font-weight:700;line-height:24px;}
.benefits ul{list-style:none;margin:0;padding:0;}
.benefits li{position:relative;padding-left:14px;font-size:17.5px;line-height:24.2px;}
.benefits li::before{content:"";position:absolute;left:2px;top:10px;width:5px;height:5px;border-radius:50%;background:var(--red);}
.benefits p{margin:14px 0 0;font-size:17.5px;line-height:24.2px;}
.benefits .emphasis{color:var(--muted);font-weight:700;margin-top:14px;}
.back-curve{position:absolute;left:0;bottom:0;}
</style>
</head>
<body>
<div class="flyer">

  <section class="panel panel--front">
    <div class="photo photo--strip" role="img" aria-label="Foto: Füße von Ballettschülerinnen in weißen Schläppchen"></div>
    <div class="brand brand--top"><span class="brand__dot"></span><span class="brand__name">Ballettschule Wendelmoor</span></div>
    <div class="photo photo--hero" role="img" aria-label="Foto: Füße in weißen Strumpfhosen und Ballettschläppchen auf hellem Boden"></div>

    <div class="band-red">
      <div class="anniv"><span class="anniv__big">40 Jahre</span><span class="anniv__small">Ballettschule Wendelmoor in Elmshagen</span></div>
      <div class="invite">Herzliche Einladung zu einer Probestunde</div>
    </div>

    <div class="offer offer--kids">
      <h3>Kinder und Jugendliche:</h3>
      <ul>
        <li>Tänzerische Früherziehung ab 3 Jahren</li>
        <li>Ballettvorbereitung ab 4 Jahren</li>
        <li>Klassisches Ballett ab 6 Jahren</li>
        <li>Klassisches Ballett mit Spitze ab 12 Jahren</li>
        <li>Jazz Tanz</li>
        <li>Step Tanz</li>
        <li>Hip Hop</li>
        <li>Berufsvorbereitung Tanz</li>
      </ul>
    </div>

    <div class="offer offer--adults">
      <h3>Erwachsene:</h3>
      <ul>
        <li>Klassisches Ballett <span class="note">(auch für Anfänger und Wiedereinsteiger)</span></li>
        <li>Jazz Tanz</li>
        <li>Step Tanz</li>
        <li>Flamenco</li>
        <li>Tänzerische Gymnastik 50+, 70+</li>
      </ul>
    </div>

    <footer class="footer">
      <svg width="555" height="304" viewBox="0 0 555 304" aria-hidden="true">
        <path d="M0 0 H555 V282 Q278 260 0 282 Z" fill="#7c7d7f"/>
      </svg>
      <div class="contact">
        <div class="contact__name">Ballettschule Wendelmoor</div>
        <div class="contact__lines">
          Inh. Marla Wendelmoor<br>
          Lindenweg 17<br>
          25499 Elmshagen-Mitte<br>
          Telefon: 0 40 00.1 23 45 67<br>
          Mobil: 0170.0 12 34 56
        </div>
        <div class="contact__web">
          info@ballettschule-wendelmoor.de<br>
          www.ballettschule-wendelmoor.de
        </div>
        <div class="contact__member">Mitglied im Bund für Tanzpädagogik</div>
      </div>
    </footer>
  </section>

  <section class="panel panel--back">
    <div class="photo photo--strip" role="img" aria-label="Foto: Füße von Ballettschülerinnen in weißen Schläppchen"></div>
    <div class="quote">"Tanz ist Nahrung<br><span class="quote__second">für Gehirn und Seele."</span></div>
    <div class="photo photo--hero" role="img" aria-label="Foto: Füße in weißen Strumpfhosen und Ballettschläppchen auf hellem Boden"></div>

    <div class="band-grey">
      <p>Im Tanz bilden Körper und Geist eine Einheit.<br>Neue Bereiche im Gehirn werden erschlossen<br>und immer wieder trainiert und gestärkt.</p>
    </div>

    <div class="gallery gallery--costumes" role="img" aria-label="Foto: Kinder in Marienkäfer-Kostümen im Ballettsaal"></div>
    <div class="gallery gallery--stage" role="img" aria-label="Foto: Kinder in rosa Tutus bei einer Aufführung im Freien"></div>

    <div class="benefits">
      <h3>Eine Grundausbildung im Klassischen Ballett führt zu:</h3>
      <ul>
        <li>gesunden Kräftigung der gesamten Muskulatur</li>
        <li>Förderung einer guten Körperhaltung</li>
        <li>erweiterter Wahrnehmungsfähigkeit</li>
        <li>Verbesserung des Konzentrationsvermögen</li>
        <li>Verstärkung des Selbstwertgefühls</li>
        <li>Disziplin, Respekt und Genauigkeit</li>
      </ul>
      <p>Besonders für Kinder unterstützt Ballettunterricht jegliche Bewegungsform und verhilft nachweislich zu besseren Schulergebnissen.</p>
      <p class="emphasis">Tanzen, Kunst und Musik fördern in Ihrer Einheit die emotionale Ausgeglichenheit und den Sinn für Grazie und Harmonie.</p>
    </div>

    <div class="brand brand--bottom"><span class="brand__dot"></span><span class="brand__name">Ballettschule Wendelmoor</span></div>

    <svg class="back-curve" width="559" height="40" viewBox="0 0 559 40" aria-hidden="true">
      <path d="M0 22 Q280 -2 559 22 V40 H0 Z" fill="#7c7d7f"/>
    </svg>
  </section>

</div>
</body>
</html>
```